Club Membership Invitation

I am wanting to create a membership flyer/rackcard/postcard that schools can send back to me.
It is to promote ICT professional development for teachers and membership to "the club" will entitle the schools to special discounts of Professional Development rates, priority seating at workshops, the opportunity to join other schools in quality ICT  professional development.
Membership is free but they will need to send the form back to get membership.
Our website is www.crossingtheriver.example. which gives a flavour/ colours of our business

Updates
Hi, Could the name please be changed to The Lantern PD Club".
Thank you for the designs.

Target Market(s)
Primary Schools, Teachers, Leadership teams
Industry/Entity Type
Business
Requirements
Must have
- I would like it to be 2 sides.
Logo
"Lighting the Path PD Club"
Free membership
www.crossingtheriver.example
0508 ICT TUTOR
Benefits of membership...
Ongoing discounts
ICT PD clustering
Termly Specials
Priority seating at workshops
Early Bird notification
The form needs the address as it will beed to be sent or handed to...
ICT PD Membership
Lighting the Path
7 Kowhaiwai Terrace
Kelmore, 4736

```html
<!DOCTYPE html>
<html lang="en">
<head>
<meta charset="utf-8">
<title>The Lantern PD Club – Membership Form</title>
<link href="https://fonts.googleapis.com/css2?family=Arimo:ital,wght@0,400;0,700;1,700&family=Tinos:ital@1&display=swap" rel="stylesheet">
<style>
  :root {
    --sky-top: #7ccaf2;
    --sky-mid: #b4e0f8;
    --sky-bottom: #e6f5fd;
    --ink: #1560bd;
    --name-blue: #1a55e0;
    --badge: #0a5bb5;
    --frame: #3b8de0;
    --paper: #ffffff;
    --grass-light: #a9d84a;
    --grass-dark: #5fa52a;
  }
  * { box-sizing: border-box; margin: 0; padding: 0; }
  html, body { width: 887px; height: 1200px; overflow: hidden; }
  body { font-family: "Arimo", Arial, sans-serif; color: var(--ink); }

  .flyer {
    position: relative; width: 887px; height: 1200px; overflow: hidden;
    background: linear-gradient(180deg, var(--sky-top) 0%, var(--sky-mid) 45%, var(--sky-bottom) 85%);
  }

  .club-name {
    position: absolute; left: 44px; top: 48px; width: 520px;
    font-family: "Arimo", Arial, sans-serif; font-weight: 700;
    font-size: 62px; line-height: 74px; color: var(--name-blue);
  }

  .tagline {
    position: absolute; left: 97px; top: 230px;
    font-family: "Arimo", Arial, sans-serif; font-weight: 400;
    font-size: 27px; color: var(--name-blue);
  }

  .badge { position: absolute; left: 580px; top: 85px; width: 270px; height: 250px; z-index: 2; }
  .badge-text { font-family: "Arimo", Arial, sans-serif; fill: #fff; }

  .form-card {
    position: absolute; left: 18px; top: 307px; width: 851px; height: 484px;
    background: var(--paper); border: 1px solid var(--frame); z-index: 1;
  }
  .form-title {
    position: absolute; left: 0; right: 0; top: 8px; text-align: center;
    font-family: "Tinos", "Times New Roman", serif; font-style: italic; font-weight: 400;
    font-size: 37px; text-decoration: underline; text-decoration-thickness: 1px;
    text-underline-offset: 5px;
  }
  .field {
    position: absolute; left: 12px; right: 22px; display: flex; align-items: baseline;
    font-size: 22px; line-height: 26px;
  }
  .field .fill { flex: 1; margin-left: 8px; border-bottom: 2px dotted var(--ink); transform: translateY(-5px); }
  .field.continued { left: 172px; }
  .field.date { right: auto; width: 230px; }
  .field.signature { left: auto; right: 22px; width: 270px; }

  .send-note {
    position: absolute; left: 28px; top: 811px;
    font-style: italic; font-weight: 700; font-size: 20px;
  }
  .return-address {
    position: absolute; left: 397px; top: 875px;
    font-style: normal; font-size: 28px; line-height: 35px;
  }

  .grass {
    position: absolute; left: 0; bottom: 0; width: 887px; height: 120px;
    background: linear-gradient(180deg, rgba(169,216,74,0) 0%, var(--grass-light) 35%, var(--grass-dark) 100%);
  }

  .footer-link, .footer-phone { position: absolute; top: 1076px; font-size: 27px; }
  .footer-link { left: 32px; }
  .footer-phone { right: 41px; }
</style>
</head>
<body>
<main class="flyer">

  <h1 class="club-name">The Lantern<br>PD Club</h1>
  <p class="tagline">Computer Training for Educators</p>

  <svg class="badge" viewBox="0 0 270 250" aria-label="Free membership">
    <polygon fill="var(--badge)" stroke="#fff" stroke-width="3" points="
      135,5 150,32 172,12 178,42 205,30 201,60 232,56 218,84 248,92 226,113
      255,130 226,145 246,168 216,173 226,202 196,199 195,230 169,215 158,244
      139,221 120,244 109,216 83,232 82,201 52,207 62,178 32,172 53,149
      24,132 52,116 30,94 60,87 48,58 78,62 75,32 102,44 110,14 128,36"/>
    <g transform="rotate(-20 135 125)">
      <text class="badge-text" x="135" y="120" text-anchor="middle" font-size="54">Free</text>
      <text class="badge-text" x="145" y="158" text-anchor="middle" font-size="28">Membership</text>
    </g>
  </svg>

  <section class="form-card">
    <h2 class="form-title">Membership Form</h2>
    <div class="field" style="top:67px"><span>School Name:</span><span class="fill"></span></div>
    <div class="field continued" style="top:114px"><span class="fill"></span></div>
    <div class="field" style="top:152px"><span>School Roll:</span><span class="fill"></span></div>
    <div class="field" style="top:194px"><span>Town/City:</span><span class="fill"></span></div>
    <div class="field" style="top:236px"><span>Region:</span><span class="fill"></span></div>
    <div class="field" style="top:276px"><span>School phone:</span><span class="fill"></span></div>
    <div class="field" style="top:313px"><span>School contact:</span><span class="fill"></span></div>
    <div class="field" style="top:353px"><span>School contact email:</span><span class="fill"></span></div>
    <div class="field date" style="top:433px"><span>Date:</span><span class="fill"></span></div>
    <div class="field signature" style="top:433px"><span>Signature:</span><span class="fill"></span></div>
  </section>

  <p class="send-note">The form needs to be sent or handed to...</p>
  <address class="return-address">
    ICT PD Membership<br>
    Lighting the Path<br>
    7 Kowhaiwai Terrace<br>
    Kelmore, 4736
  </address>

  <div class="grass" role="img" aria-label="Green grass along the bottom edge"></div>

  <p class="footer-link">www.crossingtheriver.example</p>
  <p class="footer-phone">0508 ICT TUTOR</p>

</main>
</body>
</html>
```